Luxury Brand Real Estate For Sale sign

**Update** I've added some examples from the internet of other signs that have a look similar to what I would like to see. I do not want my personal name in the sign. And the word FOR SALE Does not need to be so large - it can be more subtle.
I want to create a Real Estate for sale sign for my company that will be used for luxury/higher end real estate listings. I’m sharing my business card as well as a logo with new teal color to show what we're moving towards: we’re using Teal, white, black and gold.
Hoping the sign is simple, sophisticated and eye catching.
The sign should be 24" wide by 30" tall including the company name: Harbor Crest Realty Group and our logo, office phone number 727-555-0148 and website www.hcrgproperty.example the words "For Sale"
Optional to add this e-mail address info@hcrgproperty.example to the sign
Luxury home buyers
Real Estate

```html
<!DOCTYPE html>
<html lang="en">
<head>
<meta charset="utf-8">
<title>Harbor Crest Realty Group — For Sale Sign</title>
<link rel="stylesheet" href="https://fonts.googleapis.com/css2?family=Marcellus&family=Montserrat:wght@400&family=Poppins:wght@400;700&display=swap">
<style>
  :root {
    --teal: #06827f;
    --teal-deep: #05726f;
    --white: #ffffff;
    --mist: #e9eeed;
    --ink: #1f1b1c;
    --gold-dark: #d7a637;
    --gold-light: #f3d77c;
    --backdrop: #eceeed;
  }
  * { margin: 0; padding: 0; box-sizing: border-box; }
  html, body {
    width: 1190px;
    height: 1200px;
    overflow: hidden;
    background: var(--backdrop);
  }
  .sign {
    position: absolute;
    left: 155px;
    top: 50px;
    width: 880px;
    height: 1100px;
    background: var(--white);
    overflow: hidden;
    box-shadow: 0 6px 24px rgba(0, 0, 0, 0.12);
  }
  .sign__texture {
    position: absolute;
    inset: 0 0 auto 0;
    height: 640px;
    background:
      radial-gradient(ellipse 420px 300px at 700px 200px, var(--mist), transparent 70%),
      radial-gradient(ellipse 360px 220px at 380px 560px, var(--mist), transparent 70%),
      radial-gradient(ellipse 200px 160px at 120px 420px, #f1f4f3, transparent 70%);
  }
  .sign__shapes {
    position: absolute;
    inset: 0;
  }
  .headline {
    position: absolute;
    left: 0;
    right: 0;
    top: 22px;
    text-align: center;
    font-family: "Marcellus", serif;
    color: var(--teal);
    font-size: 272px;
    line-height: 222px;
    letter-spacing: -2px;
  }
  .headline span { display: block; }
  .brand {
    position: absolute;
    left: 130px;
    top: 730px;
    display: flex;
    align-items: center;
    gap: 22px;
  }
  .brand__square {
    width: 80px;
    height: 80px;
    border: 5px solid var(--white);
  }
  .brand__divider {
    width: 3px;
    height: 112px;
    background: var(--ink);
  }
  .brand__name {
    font-family: "Montserrat", sans-serif;
    font-weight: 400;
    color: var(--white);
    font-size: 38px;
    line-height: 46px;
    letter-spacing: 1px;
    text-transform: uppercase;
  }
  .website {
    position: absolute;
    left: 0;
    right: 0;
    top: 852px;
    text-align: center;
    font-family: "Poppins", sans-serif;
    font-weight: 400;
    color: var(--white);
    font-size: 36px;
    letter-spacing: 5px;
  }
  .phone-band {
    position: absolute;
    left: 0;
    right: 0;
    bottom: 0;
    height: 200px;
    background: linear-gradient(90deg, var(--gold-dark), var(--gold-light) 50%, var(--gold-dark));
    display: flex;
    align-items: center;
    justify-content: center;
  }
  .phone {
    font-family: "Poppins", sans-serif;
    font-weight: 700;
    color: var(--ink);
    font-size: 100px;
    letter-spacing: 1px;
  }
</style>
</head>
<body>
  <main class="sign">
    <div class="sign__texture" role="img" aria-label="Faint grey watercolor texture behind the headline"></div>

    <svg class="sign__shapes" width="880" height="1100" viewBox="0 0 880 1100" aria-hidden="true">
      <defs>
        <linearGradient id="ribbon-gold" x1="0" y1="0" x2="1" y2="0">
          <stop offset="0" stop-color="#d7a637"/>
          <stop offset="0.5" stop-color="#f3d77c"/>
          <stop offset="1" stop-color="#d7a637"/>
        </linearGradient>
      </defs>
      <path class="ribbon" fill="url(#ribbon-gold)"
            d="M0,530 C230,650 560,650 880,450 L880,520 C580,700 230,700 0,590 Z"/>
      <path class="ribbon-highlight" fill="none" stroke="#ffffff" stroke-width="5"
            d="M0,565 C230,665 520,668 760,570"/>
      <path class="teal-field" fill="var(--teal)"
            d="M0,600 C230,705 580,705 880,530 L880,1100 L0,1100 Z"/>
    </svg>

    <h1 class="headline"><span>FOR</span><span>SALE</span></h1>

    <div class="brand">
      <div class="brand__square"></div>
      <div class="brand__divider"></div>
      <div class="brand__name">Harbor Crest<br>Realty Group</div>
    </div>

    <p class="website">www.hcrgproperty.example</p>

    <div class="phone-band">
      <p class="phone">727-555-0148</p>
    </div>
  </main>
</body>
</html>
```